business card with 2 locations on 1 card

I need a modern looking business card that I would use at 2 different locations. Possibly 1 location on 1 side and other location on other side. One should be able to distinguish the 2 locations immediately before having to read the address or description on card. You can take a look at my website to see what I'm drawn to. The logo is brand new that I just purchased on Sketch Harbor. I want to emphasize family.
Updates

Let's not use the yellow and blue colors. Added Thursday, August 31, 2017

Target Market(s)

women and children

Industry/Entity Type

Health And Wellness

Contact Information for Business Card

Business name: Willow Path Chiropractic & Acupuncture
My name: Lorna Dwyer
Job title: DC, MSOM, LAc, CNS

Location 1
Address: 4817 Brinmoor Blvd, Suite C-210, Aldenport, TX 75990
Phone: (469) 555-0182
Fax: (972) 555-0147

Location 2
Address: 1936 Venlow Road, Suite 300, Marrowfield, TX 75991
Phone: (469) 555-0129
Fax: (972) 555-0147

Email: drlornadwyer@mailvessel.example
Website: www.drlornadwyer.example

Font styles to use
Serif
Sans Serif

Colors

Designer to choose colors to be used in the design.

Requirements
Must have
• distinction between 2 locations.
Nice to have
• Colors preference below is there. But I like to see what you come up with too!

```html
<!DOCTYPE html>
<html lang="en">
<head>
<meta charset="utf-8">
<title>Willow Path Chiropractic &amp; Acupuncture – Business Card</title>
<link rel="stylesheet" href="https://fonts.googleapis.com/css2?family=Montserrat:wght@400;500;700&display=swap">
<style>
  :root {
    --backdrop: #e7e5e1;
    --paper: #ffffff;
    --ink: #333333;
    --ink-soft: #444444;
    --leaf: #1e9a52;
    --leaf-pale: #b3d58d;
    --teal: #1f6b65;
    --rule: #3a3a3a;
  }
  * { box-sizing: border-box; margin: 0; padding: 0; }
  html, body { width: 1200px; height: 900px; overflow: hidden; }
  body {
    background: var(--backdrop);
    font-family: "Montserrat", sans-serif;
    color: var(--ink);
    position: relative;
  }
  .card {
    position: absolute;
    left: 250px;
    width: 700px;
    height: 400px;
    background: var(--paper);
    box-shadow: 0 6px 18px rgba(0,0,0,.18);
    overflow: hidden;
  }
  .card--front { top: 33px; }
  .card--back { top: 466px; }

  /* front */
  .holder {
    position: absolute;
    right: 70px; top: 52px;
    text-align: right;
  }
  .holder__name {
    font-weight: 700;
    font-size: 34px;
    letter-spacing: 1px;
    color: var(--ink);
    text-transform: uppercase;
  }
  .holder__title {
    font-size: 13px;
    font-weight: 500;
    color: var(--leaf);
    margin-top: 2px;
  }
  .brand-badge {
    position: absolute;
    right: 76px; top: 150px;
    display: flex; flex-direction: column; align-items: center; gap: 8px;
  }
  .brand-badge__circle {
    width: 120px; height: 120px;
    border-radius: 50%;
    border: 6px solid var(--teal);
  }
  .brand-badge__name {
    font-size: 14px; font-weight: 500; color: var(--teal);
  }
  .locations {
    position: absolute;
    left: 48px; top: 118px;
    display: flex; flex-direction: column; gap: 26px;
  }
  .location {
    border-left: 2px solid var(--rule);
    padding-left: 18px;
    font-size: 15px;
    line-height: 1.3;
    color: var(--ink-soft);
  }
  .location__address { margin-bottom: 8px; margin-left: -6px; }
  .contact-line { display: flex; align-items: center; gap: 12px; }
  .contact-line svg { width: 16px; height: 16px; flex: none; }

  /* back */
  .brand-lockup {
    position: absolute;
    left: 0; right: 0; top: 70px;
    display: flex; flex-direction: column; align-items: center;
  }
  .brand-lockup__circle {
    width: 140px; height: 140px;
    border-radius: 50%;
    border: 7px solid var(--teal);
    margin-bottom: 22px;
  }
  .brand-lockup__name {
    font-size: 40px; font-weight: 500; color: var(--teal);
    letter-spacing: 2px; text-transform: uppercase;
  }
  .brand-lockup__service {
    font-size: 15px; font-weight: 500; color: var(--teal);
    letter-spacing: 2.5px; text-transform: uppercase; margin-top: 2px;
  }
  .color-band {
    position: absolute; left: 0; right: 0; bottom: 0; height: 60px;
    display: flex;
  }
  .color-band__leaf { width: 280px; background: var(--leaf); }
  .color-band__pale { width: 150px; background: var(--leaf-pale); }
  .color-band__web {
    flex: 1; background: var(--teal); color: #fff;
    font-size: 17px; letter-spacing: .5px;
    display: flex; align-items: center; justify-content: center;
  }
</style>
</head>
<body>

<section class="card card--front" aria-label="Card front">
  <div class="holder">
    <h1 class="holder__name">Lorna Dwyer</h1>
    <p class="holder__title">DC, MSOM, LAc, CNS</p>
  </div>

  <div class="brand-badge">
    <div class="brand-badge__circle"></div>
    <span class="brand-badge__name">Willow Path</span>
  </div>

  <div class="locations">
    <div class="location">
      <p class="location__address">4817 Brinmoor Blvd,<br>Suite C-210, Aldenport, TX 75990</p>
      <p class="contact-line">
        <svg viewBox="0 0 16 16"><path fill="var(--leaf)" d="M3 1l3 3-1.6 1.8a9 9 0 006 6L12.2 10l3 3-2 2C7 15 1 9 1 3z"/></svg>
        (469) 555-0182</p>
      <p class="contact-line">
        <svg viewBox="0 0 16 16"><rect x="4" y="1" width="8" height="5" fill="none" stroke="var(--leaf)" stroke-width="1.5"/><rect x="1" y="6" width="14" height="6" fill="var(--leaf)"/><rect x="4" y="10" width="8" height="5" fill="#fff" stroke="var(--leaf)" stroke-width="1.5"/></svg>
        (972) 555-0147</p>
    </div>

    <div class="location">
      <p class="location__address">1936 Venlow Road,<br>Suite 300, Marrowfield, TX 75991</p>
      <p class="contact-line">
        <svg viewBox="0 0 16 16"><path fill="var(--leaf)" d="M3 1l3 3-1.6 1.8a9 9 0 006 6L12.2 10l3 3-2 2C7 15 1 9 1 3z"/></svg>
        (469) 555-0129</p>
      <p class="contact-line">
        <svg viewBox="0 0 16 16"><rect x="4" y="1" width="8" height="5" fill="none" stroke="var(--leaf)" stroke-width="1.5"/><rect x="1" y="6" width="14" height="6" fill="var(--leaf)"/><rect x="4" y="10" width="8" height="5" fill="#fff" stroke="var(--leaf)" stroke-width="1.5"/></svg>
        (972) 555-0147</p>
      <p class="contact-line">
        <svg viewBox="0 0 16 16"><rect x="1" y="3" width="14" height="10" fill="none" stroke="var(--leaf)" stroke-width="1.6"/><path d="M1 3l7 6 7-6" fill="none" stroke="var(--leaf)" stroke-width="1.6"/></svg>
        drlornadwyer@mailvessel.example</p>
      <p class="contact-line">
        <svg viewBox="0 0 16 16"><circle cx="8" cy="8" r="7" fill="none" stroke="var(--leaf)" stroke-width="1.5"/><ellipse cx="8" cy="8" rx="3" ry="7" fill="none" stroke="var(--leaf)" stroke-width="1.2"/><path d="M1 8h14M2.5 4.5h11M2.5 11.5h11" stroke="var(--leaf)" stroke-width="1.2"/></svg>
        www.drlornadwyer.example</p>
    </div>
  </div>
</section>

<section class="card card--back" aria-label="Card back">
  <div class="brand-lockup">
    <div class="brand-lockup__circle"></div>
    <p class="brand-lockup__name">Willow Path</p>
    <p class="brand-lockup__service">Chiropractic &amp; Acupuncture</p>
  </div>
  <div class="color-band">
    <div class="color-band__leaf"></div>
    <div class="color-band__pale"></div>
    <div class="color-band__web">www.drlornadwyer.example</div>
  </div>
</section>

</body>
</html>
```